BrovaLT BIZ Card, email signature & Stationary

Professional business cards, email signatures and ms word letterhead

Target Market(s)

business owners

Industry/Entity Type

cloud hosting

Contact Information for Business Card

name title office phone number , direct line, fax email address web site

Font styles to use
Other font styles liked:
• something that compliments font in logo

```html
<!DOCTYPE html>
<html lang="en">
<head>
<meta charset="utf-8">
<title>BrovaLT Letterhead</title>
<link rel="stylesheet" href="https://fonts.googleapis.com/css2?family=Arimo:wght@400;700&family=Mulish:wght@600;700&family=Questrial&display=swap">
<style>
  :root {
    --backdrop: #e2e2e2;
    --paper: #ffffff;
    --ink: #505050;
    --bar-dark: #231f20;
    --brand-red: #ed1c24;
    --rule: #8a8a8a;
    --sign-tone: #d9d9d9;
  }
  * { margin: 0; padding: 0; box-sizing: border-box; }
  html, body {
    width: 1153px; height: 1200px; overflow: hidden;
    background: var(--backdrop);
  }
  .letterhead {
    position: absolute; left: 173px; top: 30px;
    width: 806px; height: 1140px;
    background: var(--paper);
    color: var(--ink);
    font-family: "Arimo", Arial, sans-serif;
  }
  .top-bar { position: absolute; top: 0; height: 18px; }
  .top-bar--left { left: 0; width: 265px; background: var(--bar-dark); }
  .top-bar--center { left: 271px; width: 265px; background: var(--brand-red); }
  .top-bar--right { left: 542px; width: 264px; background: var(--bar-dark); }
  .brand-name {
    position: absolute; top: 28px; left: 0; width: 100%;
    text-align: center;
    font-family: "Questrial", sans-serif;
    font-size: 74px; line-height: 1;
    color: var(--brand-red);
    letter-spacing: -1px;
  }
  .salutation {
    position: absolute; left: 73px; top: 352px;
    font-family: "Mulish", sans-serif; font-weight: 700;
    font-size: 19px;
  }
  .letter-body { position: absolute; left: 72px; top: 411px; width: 662px; }
  .letter-body p {
    font-size: 13.5px; line-height: 16.6px;
    margin-bottom: 14.5px;
  }
  .closing {
    position: absolute; left: 73px; top: 746px;
    font-family: "Mulish", sans-serif; font-weight: 700; font-size: 11px;
  }
  .signature {
    position: absolute; left: 68px; top: 797px;
    width: 100px; height: 34px;
    background: var(--sign-tone); border-radius: 3px;
  }
  .footer { position: absolute; left: 187px; top: 1066px; width: 432px; }
  .footer-address {
    text-align: center; font-size: 13.5px; height: 21px;
    border-bottom: 1px solid var(--rule);
  }
  .footer-contacts {
    display: flex; justify-content: space-between; align-items: center;
    margin-top: 6px; font-size: 13.5px;
  }
  .contact-item { display: flex; align-items: center; gap: 5px; }
  .contact-item svg { width: 10px; height: 10px; fill: var(--brand-red); }
</style>
</head>
<body>
<main class="letterhead">
  <div class="top-bar top-bar--left"></div>
  <div class="top-bar top-bar--center"></div>
  <div class="top-bar top-bar--right"></div>

  <h1 class="brand-name">BrovaLT</h1>

  <h2 class="salutation">Dear Mr. Hallow,</h2>

  <section class="letter-body">
    <p>Lorem ipsum dolor sit amet, consectetuer adipiscing elit, sed diam nonmmy nibh euismod tincidunt ut laor eet dolore magna aliquam erat volutpat. Ut wisi enim ad minim veniam, quis nostrud exerci tationmcorper suscipit lobortis nisl ut aliquip ex ea commodo consequat. Duis autem vel eum iriure dolor in hendrerit in vulputate velit esse molestie consequat, vel illum dolore eu feugiat</p>
    <p>Rorem ipsum dolor sit amet, consectetuer adipiscing elit, sed diam nonmmy nibh euismod tincidunt ut laor eet dolore magna aliquam erat volutpat. Ut wisi enim ad minim veniam, quis nostrud exerci tationmcorper suscipit lobortis nisl ut aliquip ex ea commodo consequat. Duis autem vel eum iriure dolor in hendrerit in vulputate velit esse molest</p>
    <p>Dorem ipsum dolor sit amet, consectetuer adipiscing elit, sed diam nonmmy nibh euismod tincidunt ut laor eet dolore magna aliquam erat volutpat. Ut wisi enim ad minim veniam, quis nostrud exerci tationmcorper suscipit lobortis nisl ut aliquip ex ea commodo consequat. Duis autem vel eum iriure dolor in hendrerit in suscipit lobortis nisl ut aliquip ex ea commodo consequat. Duis autem vel eum iriure dolor in hendrerit in vulputate velit esse molestie consequat, vel illum</p>
    <p>Sorem ipsum dolor sit amet, consectetuer adipiscing elit, sed diam nonmmy nibh euismod tincidunt ut laor eet dolore magna aliquam erat volutpat. Ut wisi enim ad minim veniam, quis nostrud exerci tationmcorper suscipit lobortis nisl ut aliquip ex ea commodo consequat. Duis autem vel eum iriure dolor in</p>
  </section>

  <p class="closing">Sincerely,</p>
  <div class="signature" role="img" aria-label="Handwritten signature of the sender"></div>

  <footer class="footer">
    <p class="footer-address">Your address, city, state, ZIP 0000</p>
    <div class="footer-contacts">
      <span class="contact-item">
        <svg viewBox="0 0 10 10" aria-hidden="true"><path d="M2 0.5 L3.6 2.6 L2.7 3.6 Q3.8 5.9 6.3 7.3 L7.4 6.4 L9.5 8 L8.3 9.5 Q3.6 9 0.5 1.7 Z"/></svg>
        123-456-2100
      </span>
      <span class="contact-item">
        <svg viewBox="0 0 10 10" aria-hidden="true"><path d="M0.5 2 H9.5 V8 H0.5 Z M1.3 2.6 L5 5.4 L8.7 2.6" stroke="#fff" stroke-width="0.8"/></svg>
        youremail@brovalt.com
      </span>
      <span class="contact-item">
        <svg viewBox="0 0 10 10" aria-hidden="true"><circle cx="5" cy="5" r="4.5"/><circle cx="5" cy="5" r="1.8" fill="#fff"/></svg>
        www.yourwebsite.com
      </span>
    </div>
  </footer>
</main>
</body>
</html>
```